Web-Design for Electrcian Company

Our Customer is a small business electrian in Switzerland. He is looking for a fresh and innovative website design. He is well known for his extra service, and that they always go for the extra-mile! In his logo you also see that positive and fresh image the try to bring to the customer. the main colors are black, red and white.

the website structure will be:

- home
- services (with submenu for each service)
- references (with submenu for each category of services)
- about us (2 submenus: history and staff)
- links
- Contact

Reason: We are discussing the Proposals with the customer right now

Target Market(s)

Architects, building owners, people from the age of 35 up...

Industry/Entity Type

Small Business

```html
<!DOCTYPE html>
<html lang="en">
<head>
<meta charset="utf-8">
<title>Brunner + Meier Elektro AG</title>
<link href="https://fonts.googleapis.com/css2?family=Open+Sans:wght@400;600;700&family=Rokkitt:wght@400;500&display=swap" rel="stylesheet">
<style>
:root{
  --red:#d9232d;
  --red-dark:#b81c25;
  --ink:#1f1f1f;
  --dark:#232323;
  --darker:#1a1a1a;
  --light:#e8e8e8;
  --muted:#777;
  --white:#fff;
  --footer-text:#c9c9c9;
}
*{margin:0;padding:0;box-sizing:border-box}
html,body{width:909px;height:1200px;overflow:hidden}
body{position:relative;font-family:'Open Sans',sans-serif;background:var(--light);color:var(--muted)}
.abs{position:absolute}
.slab{font-family:'Rokkitt',serif;font-weight:500}

/* header */
.site-header{left:0;top:0;width:909px;height:89px;background:linear-gradient(#202020,#151515);border-bottom:1px solid #333}
.brand{left:29px;top:29px;color:var(--white);font-size:20px;font-weight:600;letter-spacing:.2px}
.brand-mark{left:310px;top:6px;width:76px;height:76px;border:3px solid var(--red);border-radius:50%}
.main-nav{right:18px;top:31px;display:flex;gap:18px;font-size:15px}
.main-nav a{color:#ddd;text-decoration:none;padding:4px 0}
.main-nav a.active{background:var(--red);color:var(--white);padding:4px 9px}

/* hero */
.hero{left:0;top:89px;width:909px;height:383px;background:linear-gradient(#e22a33,#cc222b 60%,#c2202a)}
.hero-title{left:89px;top:36px;font-size:37px;color:var(--white);line-height:1;font-weight:400}
.hero-sub{left:136px;top:76px;font-size:37px;color:#2a2a2a;line-height:1;font-weight:400}
.arrow{width:44px;height:44px;border-radius:50%;background:var(--white);top:109px}
.arrow svg{position:absolute;left:12px;top:12px}
.slide{background:var(--white);padding:4px}
.slide .photo{width:100%;height:calc(100% - 24px)}
.slide .caption{background:#111;color:var(--white);text-align:center;font-size:13px;height:24px;line-height:24px}
.slide.center .photo{height:calc(100% - 32px)}
.slide.center .caption{height:32px;line-height:32px;font-size:15px}
.hero-shade{left:89px;top:362px;width:731px;height:20px;background:linear-gradient(rgba(0,0,0,.08),rgba(0,0,0,0))}
.divider-shadow{left:80px;top:474px;width:750px;height:6px;background:radial-gradient(ellipse at center,rgba(0,0,0,.28),rgba(0,0,0,0) 70%)}

/* content */
.block-title{font-size:27px;color:var(--red);font-weight:400;line-height:1}
.block-text{font-size:13px;line-height:19.5px;color:var(--muted);width:420px}
.col-rule{left:455px;top:516px;width:1px;height:224px;background:#c9c9c9}
.quote-text{left:134px;top:711px;font-size:13px;line-height:20px;color:var(--red)}
.thumb{width:80px;height:80px;border:2px solid #333;background:var(--white)}
.thumb .fill{width:100%;height:100%}
.thumb-label{font-size:13px;line-height:16px;color:#666;width:90px}
.social{display:flex;gap:6px}
.social span{width:14px;height:14px;border-radius:50%;background:#2a8fd0}

/* footer */
.site-footer{left:0;top:790px;width:909px;height:377px;background:var(--dark)}
.foot-title{font-size:28px;color:var(--white);font-weight:400;line-height:1}
.foot-sub{font-size:13px;color:var(--footer-text)}
.foot-rule{height:1px;background:#3a3a3a}
.field{left:31px;width:187px;background:#141414;border:1px solid #3a3a3a;border-radius:2px;color:#888;font-size:13px;padding:2px 12px}
.btn{height:27px;background:var(--red);color:var(--white);font-weight:700;font-size:14px;border-radius:3px;display:flex;align-items:center;justify-content:center;gap:16px}
.btn i{width:13px;height:13px;border-radius:50%;background:#111;display:inline-block;position:relative}
.btn i::after{content:"";position:absolute;left:4px;top:3.5px;border-left:5px solid #fff;border-top:3px solid transparent;border-bottom:3px solid transparent}
.news{font-size:14px;color:var(--white);line-height:21px}
.news b{font-weight:700}
.news p{font-size:14px;line-height:18px;color:#e6e6e6;font-weight:400}

/* bottom bar */
.bottom-bar{left:0;top:1167px;width:909px;height:33px;background:var(--darker);border-top:1px solid #333}
.copyright{left:32px;top:8px;font-size:14px;color:#ddd}
.copyright b{color:var(--white)}
.foot-nav{right:22px;top:8px;font-size:14px;color:#ddd}
.foot-nav a{color:#ddd;text-decoration:none}
.foot-nav a.active{color:var(--red)}
.foot-nav .sep{margin:0 8px}
</style>
</head>
<body>

<header class="abs site-header">
  <div class="abs brand">Brunner + Meier Elektro AG</div>
  <div class="abs brand-mark"></div>
  <nav class="abs main-nav">
    <a class="active" href="#">home</a><a href="#">services</a><a href="#">references</a><a href="#">about us</a><a href="#">links</a><a href="#">contact</a>
  </nav>
</header>

<section class="abs hero">
  <h1 class="abs hero-title slab">Herzlich willkommen!</h1>
  <h2 class="abs hero-sub slab">Welcome!</h2>
  <div class="abs arrow" style="left:27px"><svg width="20" height="20" viewBox="0 0 20 20"><path d="M13 3 L6 10 L13 17" stroke="#c8202a" stroke-width="4" fill="none"/></svg></div>
  <div class="abs arrow" style="left:838px"><svg width="20" height="20" viewBox="0 0 20 20"><path d="M7 3 L14 10 L7 17" stroke="#c8202a" stroke-width="4" fill="none"/></svg></div>

  <div class="abs slide" style="left:89px;top:182px;width:214px;height:130px">
    <div class="photo" role="img" aria-label="Electrician working on a cable panel" style="background:linear-gradient(135deg,#2c4a7a,#8a9bb0 50%,#d48a2a)"></div>
    <div class="caption">Featured service goes here</div>
  </div>
  <div class="abs slide" style="left:606px;top:182px;width:214px;height:130px">
    <div class="photo" role="img" aria-label="Two electricians checking a control cabinet" style="background:linear-gradient(135deg,#4a5a78,#2b3d6a 55%,#6f8a5a)"></div>
    <div class="caption">Featured service goes here</div>
  </div>
  <div class="abs slide center" style="left:303px;top:153px;width:303px;height:177px">
    <div class="photo" role="img" aria-label="Electrician installing wiring in a timber frame" style="background:linear-gradient(135deg,#3a2414,#9a6a3a 50%,#c23226)"></div>
    <div class="caption">Featured service goes here</div>
  </div>
  <div class="abs hero-shade"></div>
</section>
<div class="abs divider-shadow"></div>

<section>
  <h3 class="abs block-title slab" style="left:31px;top:504px">Title one goes here</h3>
  <p class="abs block-text" style="left:31px;top:536px">Perpetua praesent dissentiet et est, nam essent verterem in, ut eos novum aliquip repudiandae. Alia concludaturque sed cu. Cum fugit offendit ponderum an. Eam et iisque voluptaria efficiendi, in</p>
  <h3 class="abs block-title slab" style="left:31px;top:612px">Title three goes here</h3>
  <p class="abs block-text" style="left:31px;top:644px">Perpetua praesent dissentiet et est, nam essent verterem in, ut eos novum aliquip repudiandae. Alia concludaturque sed cu. Cum</p>
  <svg class="abs" style="left:44px;top:704px" width="68" height="64" viewBox="0 0 68 64">
    <path d="M2 62 C-2 40 8 14 30 2 L32 6 C20 16 18 26 22 34 C30 34 34 42 32 52 C30 62 8 66 2 62 Z" fill="#b81c25"/>
    <path d="M36 62 C32 40 42 14 64 2 L66 6 C54 16 52 26 56 34 C64 34 68 42 66 52 C64 62 42 66 36 62 Z" fill="#b81c25"/>
  </svg>
  <p class="abs quote-text">Laboramus accommodare qui ad, suscipit<br>vulputate theophrastus an his, mei movet epicuri</p>

  <div class="abs col-rule"></div>

  <h3 class="abs block-title slab" style="left:485px;top:504px">Title two goes here</h3>
  <p class="abs block-text" style="left:485px;top:536px;width:405px">Perpetua praesent dissentiet et est, nam essent verterem in, ut eos novum aliquip repudiandae. Alia concludaturque sed cu. Cum fugit offendit ponderum an. Eam et iisque voluptaria efficiendi, in</p>

  <div class="abs thumb" style="left:486px;top:607px"><div class="fill" role="img" aria-label="Green power plug" style="background:radial-gradient(circle,#a6d63a,#e8f0d8 70%)"></div></div>
  <div class="abs thumb" style="left:602px;top:607px"><div class="fill" role="img" aria-label="Red multimeter" style="background:radial-gradient(circle,#d8303a,#f0e4e4 70%)"></div></div>
  <div class="abs thumb" style="left:718px;top:607px"><div class="fill" role="img" aria-label="Coloured cable coils" style="background:linear-gradient(90deg,#e6c43a,#d8523a,#6aa84a,#e6c43a)"></div></div>

  <p class="abs thumb-label" style="left:486px;top:696px">Another subtitle here</p>
  <p class="abs thumb-label" style="left:602px;top:696px">Another subtitle here</p>
  <p class="abs thumb-label" style="left:718px;top:696px">Another subtitle here</p>
  <div class="abs social" style="left:486px;top:738px"><span></span><span></span><span></span></div>
  <div class="abs social" style="left:602px;top:738px"><span></span><span></span><span></span></div>
  <div class="abs social" style="left:718px;top:738px"><span></span><span></span><span></span></div>
</section>

<footer class="abs site-footer">
  <h3 class="abs foot-title slab" style="left:31px;top:40px">Contact us</h3>
  <p class="abs foot-sub" style="left:31px;top:76px">Use the form below to send us a message</p>
  <div class="abs foot-rule" style="left:31px;top:101px;width:258px"></div>
  <div class="abs field" style="top:127px;height:22px">Name</div>
  <div class="abs field" style="top:159px;height:22px">E-mail</div>
  <div class="abs field" style="top:192px;height:97px;padding-top:4px">Message</div>
  <div class="abs btn" style="left:31px;top:306px;width:107px">Send <i></i></div>

  <h3 class="abs foot-title slab" style="left:323px;top:40px">Id cum nostrum</h3>
  <p class="abs foot-sub" style="left:324px;top:76px">Id cum hinc nostrum</p>
  <div class="abs foot-rule" style="left:324px;top:101px;width:261px"></div>
  <div class="abs news" style="left:324px;top:118px"><b>Qui blandit assentior</b><br><b>Sep 18th 2012</b><p>Mei et audire admodum feugait.</p></div>
  <div class="abs news" style="left:324px;top:196px"><b>Qui blandit assentior</b><br><b>Sep 18th 2012</b><p>Mei et audire admodum feugait.</p></div>
  <div class="abs news" style="left:324px;top:278px"><b>Qui blandit assentior</b><br><b>Sep 18th 2012</b><p>Mei et audire admodum feugait.</p></div>

  <h3 class="abs foot-title slab" style="left:619px;top:40px">Latest info</h3>
  <p class="abs foot-sub" style="left:619px;top:76px">Your company's latest news</p>
  <div class="abs foot-rule" style="left:619px;top:101px;width:258px"></div>
  <div class="abs news" style="left:619px;top:118px;width:260px"><b>Subtitle goes here</b><br><b>05.07.2012.</b><p>Mei et audire admodum feugait. Mei tincidunt elaboraret no. An duo regione</p></div>
  <div class="abs news" style="left:619px;top:208px;width:260px"><b>Subtitle goes here</b><br><b>05.07.2012.</b><p>Mei et audire admodum feugait. Mei tincidunt elaboraret no. An duo regione</p></div>
  <div class="abs btn" style="left:619px;top:306px;width:107px">See more <i></i></div>
</footer>

<div class="abs bottom-bar">
  <p class="abs copyright">Copyright 2012 - <b>Brunner + Meier Elektro AG</b></p>
  <nav class="abs foot-nav">
    <a class="active" href="#">Home</a><span class="sep">|</span><a href="#">Services</a><span class="sep">|</span><a href="#">References</a><span class="sep">|</span><a href="#">About us</a><span class="sep">|</span><a href="#">Links</a><span class="sep">|</span><a href="#">Contact</a>
  </nav>
</div>

</body>
</html>
```